Restaurant Bar website in Oakland

Landing page that looks good on mobile and home. Easy to make changes to SEO and Menu page .
Might link with online ordering through the point of sale provider or not. Either way we want to be able to upload menus.
No forms need. Just landing page, about page with a paragraph and a few photos, address, hours and a mailto info@
A press page and an faq

Target Market(s)

Customers

Coding

Coded - Design and coding required

Number of Pages Required

4 page

Colors
00a990
ffc214

Requirements
Must have
• Simple to scroll
SEO
Simple to add menus
Our logo

```html
<!DOCTYPE html>
<html lang="en">
<head>
<meta charset="utf-8">
<title>Dunmore's — Restaurant &amp; Bar, Oakland</title>
<link rel="stylesheet" href="https://fonts.googleapis.com/css2?family=Playfair+Display:wght@400;700&family=Montserrat:wght@400;500;600&display=swap">
<style>
:root{
  --green-dark:#1f3a1c;
  --green-deep:#17301a;
  --gold:#c9a15a;
  --gold-soft:#d7b374;
  --ink:#222222;
  --muted:#8a8a8a;
  --paper:#ffffff;
  --mist:#f6f6f4;
  --night:#1a1a1a;
  --panel:rgba(28,28,28,.92);
}
*{box-sizing:border-box;margin:0;padding:0}
html,body{width:1200px;height:5316px;overflow:hidden}
body{font-family:"Montserrat",sans-serif;color:var(--ink);background:var(--paper);position:relative}
section,header,footer,.footer-bar{position:absolute;left:0;width:1200px}
.photo{position:absolute}

/* nav */
.site-nav{top:0;height:100px;background:var(--green-dark);display:flex;align-items:center;justify-content:space-between;padding:0 120px;z-index:2}
.brand{font-family:"Playfair Display",serif;font-weight:700;color:var(--gold);font-size:30px;letter-spacing:2px;display:flex;align-items:center;gap:12px}
.brand-dot{width:14px;height:14px;background:var(--gold);border-radius:50%}
.nav-links{display:flex;gap:34px;list-style:none}
.nav-links li{color:var(--gold);font-size:13px;font-weight:600;letter-spacing:1.5px}

/* hero */
.hero{top:100px;height:540px;background:linear-gradient(135deg,#3b3026,#5a4634 40%,#2e2a24 70%,#4a3b2c)}
.hero-shade{position:absolute;inset:0;background:rgba(20,18,15,.55)}
.hero-content{position:relative;text-align:center;color:#fff;padding-top:90px}
.hero-title{font-family:"Playfair Display",serif;font-size:68px;line-height:1.3;font-weight:400}
.hero-lede{width:620px;margin:40px auto 0;font-size:15px;line-height:1.75;color:#e4e0da}
.hero-actions{display:flex;justify-content:center;gap:24px;margin-top:50px}
.btn{display:inline-block;padding:9px 22px;font-size:12px;letter-spacing:1.5px;font-weight:600;text-transform:uppercase}
.btn-outline{border:2px solid #fff;color:#fff}
.btn-gold{background:var(--gold);color:#fff;border:2px solid var(--gold)}
.hero-arrow{display:block;margin:22px auto 0}

/* story */
.story{top:640px;height:1040px;background:var(--paper)}
.eyebrow{font-size:12px;letter-spacing:3px;color:var(--muted);text-transform:uppercase}
.story .eyebrow{position:absolute;left:120px;top:192px}
.story-title{position:absolute;left:120px;top:252px;font-family:"Playfair Display",serif;font-size:46px;font-weight:400}
.story-photo-left{left:120px;top:340px;width:452px;height:300px;background:linear-gradient(135deg,#4a3526,#8a6240 50%,#2e2219)}
.story-photo-right{left:628px;top:120px;width:452px;height:680px;background:linear-gradient(160deg,#7a5634,#a4643a 45%,#5b3b22)}
.story-text{position:absolute;font-size:15px;line-height:1.9;color:var(--muted)}
.story-text.left{left:120px;top:672px;width:452px}
.story-text.right{left:628px;top:832px;width:452px}

/* experience */
.experience{top:1680px;height:540px;background:var(--mist);text-align:center}
.experience .eyebrow{margin-top:128px}
.experience-title{font-family:"Playfair Display",serif;font-size:46px;font-weight:400;margin-top:48px}
.experience-lede{width:620px;margin:24px auto 0;font-size:15px;line-height:1.75;color:var(--muted)}
.experience .btn{margin-top:34px}

/* menu grid */
.menu-grid-band{top:2220px;height:1292px;background:var(--night)}
.menu-grid{position:absolute;left:120px;top:4px;width:960px;display:grid;grid-template-columns:repeat(3,320px);grid-template-rows:repeat(4,322px)}
.dish{background:#fff;text-align:center;padding:44px 34px 0}
.dish-price{color:var(--gold);font-size:22px;font-family:"Playfair Display",serif}
.dish-name{font-family:"Playfair Display",serif;font-size:24px;font-weight:700;margin-top:18px}
.dish-name.gold{color:var(--gold);font-family:"Montserrat",sans-serif;font-weight:500;font-size:22px;letter-spacing:2px;margin-top:0}
.dish-desc{font-size:13px;line-height:1.8;color:var(--muted);margin-top:18px}
.dish-photo{position:relative}

/* reviews */
.reviews{top:3512px;height:648px;background:var(--paper)}
.menu-link{position:absolute;left:492px;top:62px;border:2px solid var(--ink);padding:9px 22px;font-size:16px;font-weight:500}
.reviews-title{position:absolute;width:100%;top:136px;text-align:center;font-family:"Playfair Display",serif;font-size:46px;font-weight:400}
.review-row{position:absolute;left:120px;top:248px;width:960px;display:grid;grid-template-columns:repeat(4,1fr);gap:40px}
.stars{display:block}
.review-title{font-family:"Playfair Display",serif;font-size:22px;margin-top:28px;line-height:1.35}
.review-text{font-size:14px;line-height:1.8;color:var(--muted);margin-top:24px}

/* info */
.info{top:4160px;height:640px;background:linear-gradient(135deg,#223021,#3a4a33 40%,#1c2419 70%,#2f3a2a)}
.info-shade{position:absolute;inset:0;background:rgba(10,12,10,.45)}
.info-card{position:absolute;top:120px;height:400px;background:var(--panel);color:#fff;text-align:center}
.info-card.hours{left:120px;width:452px}
.info-card.visit{left:628px;width:452px}
.info-heading{font-family:"Playfair Display",serif;font-size:30px;font-weight:400;margin-top:44px}
.info-day{font-size:12px;font-weight:600;letter-spacing:2px;margin-top:26px}
.info-line{font-size:13px;line-height:1.8;color:#d8d8d8}
.visit .info-line{margin-top:16px;font-size:14px}

/* footer */
.site-footer{top:4800px;height:452px;background:var(--paper)}
.footer-brand{position:absolute;left:130px;top:72px;width:220px;font-family:"Playfair Display",serif;font-weight:700;font-size:26px;color:var(--gold);letter-spacing:1px;white-space:nowrap}
.footer-col{position:absolute;top:72px;font-size:13px;color:var(--muted);line-height:2.3}
.footer-col h4{font-family:"Montserrat",sans-serif;font-weight:500;font-size:15px;color:var(--ink);margin-bottom:8px}
.footer-col.faq{left:372px;width:220px}
.footer-col.meal{left:628px;width:220px}
.footer-col.contact{left:880px;width:200px}
.meal-photo{position:relative;width:180px;height:120px;background:linear-gradient(135deg,#6b7a3a,#c7b07a 50%,#8a5a2a)}
.meal-caption{font-size:11px;line-height:1.6;text-align:center;width:180px;margin-top:8px}
.socials{display:flex;gap:12px;margin-top:18px}
.socials span{width:16px;height:16px;border-radius:50%;background:var(--green-dark)}
.footer-bar{top:5252px;height:64px;background:var(--green-deep);color:#b9c2b3;font-size:12px;display:flex;align-items:center;padding-left:120px}
</style>
</head>
<body>

<header class="site-nav">
  <div class="brand"><span class="brand-dot"></span>DUNMORE'S</div>
  <ul class="nav-links"><li>HOME</li><li>ABOUT</li><li>DRINKS</li><li>FAQ</li><li>PRESS</li></ul>
</header>

<section class="hero" role="img" aria-label="Warm photo of a set dinner table with plates and drinks">
  <div class="hero-shade"></div>
  <div class="hero-content">
    <h1 class="hero-title">Restaurant &amp; Bar<br>~Oakland~</h1>
    <p class="hero-lede">Sed ut perspiciatis unde omnis iste natus error sit voluptatem accusantium doloremque laudantium, totam rem aperiam, eaque ipsa quae ab illo inventore veritatis et quasi architecto beatae vitae dicta sunt explicabo.</p>
    <div class="hero-actions"><span class="btn btn-outline">View Menu</span><span class="btn btn-gold">Reservations</span></div>
    <svg class="hero-arrow" width="20" height="28" viewBox="0 0 20 28"><path d="M10 2v22M3 17l7 7 7-7" stroke="#fff" stroke-width="2" fill="none"/></svg>
  </div>
</section>

<section class="story">
  <p class="eyebrow">Our Story</p>
  <h2 class="story-title">Welcome to Dunmore's</h2>
  <div class="photo story-photo-left" role="img" aria-label="Bartender pouring drinks at the bar"></div>
  <div class="photo story-photo-right" role="img" aria-label="Bowl of stew with carrots and potatoes"></div>
  <p class="story-text left">Sed ut perspiciatis unde omnis iste natus error sit voluptatem accusantium doloremque laudantium, totam rem aperiam, eaque ipsa quae ab illo inventore veritatis et quasi architecto beatae vitae dicta sunt explicabo. Nemo enim ipsam voluptatem quia voluptas sit aspernatur aut odit aut fugit, sed quia consequuntur magni dolores eos qui ratione voluptatem sequi nesciunt.</p>
  <p class="story-text right">Sed ut perspiciatis unde omnis iste natus error sit voluptatem accusantium doloremque laudantium, totam rem aperiam, eaque ipsa quae ab illo inventore.</p>
</section>

<section class="experience">
  <p class="eyebrow">Only the Best</p>
  <h2 class="experience-title">Our Top Class Experience</h2>
  <p class="experience-lede">Lorem ipsum dolor sit amet, consectetur adipiscing elit, sed do eiusmod tempor incididunt ut labore et dolore magna aliqua. Ut enim ad minim veniam, quis nostrud exercitation ullamco laboris.</p>
  <span class="btn btn-gold">View Our Menu</span>
</section>

<section class="menu-grid-band">
  <div class="menu-grid">
    <div class="dish"><p class="dish-price">$26.50</p><h3 class="dish-name">Special 1</h3><p class="dish-desc">Sed ut perspiciatis unde omnis iste natus error sit voluptatem accusantium doloremque laudantium, totam rem aperiam, eaque ipsa quae ab illo inventore veritatis et quasi architecto beatae vitae dicta.</p></div>
    <div class="dish-photo" role="img" aria-label="Wheel of cheese on a wooden board" style="background:linear-gradient(135deg,#5a4a36,#d6c08a 50%,#6a5538)"></div>
    <div class="dish"><p class="dish-price">$33.50</p><h3 class="dish-name">Special 2</h3><p class="dish-desc">Sed ut perspiciatis unde omnis iste natus error sit voluptatem accusantium doloremque laudantium, totam rem aperiam, eaque ipsa quae ab illo inventore veritatis et quasi architecto beatae vitae dicta.</p></div>

    <div class="dish-photo" role="img" aria-label="Frothy mug of beer" style="background:linear-gradient(180deg,#e8e2cf 0%,#d29a2c 35%,#8a5a14 80%,#2a1d10)"></div>
    <div class="dish"><p class="dish-price">$40.50</p><h3 class="dish-name">Bar Special</h3><p class="dish-desc">Sed ut perspiciatis unde omnis iste natus error sit voluptatem accusantium doloremque laudantium, totam rem aperiam, eaque ipsa quae ab illo inventore veritatis et quasi architecto beatae vitae dicta.</p></div>
    <div class="dish-photo" role="img" aria-label="Frothy mug of beer" style="background:linear-gradient(180deg,#e8e2cf 0%,#d29a2c 35%,#8a5a14 80%,#2a1d10)"></div>

    <div class="dish"><p class="dish-price">$40.50</p><h3 class="dish-name">House Special</h3><p class="dish-desc">Sed ut perspiciatis unde omnis iste natus error sit voluptatem accusantium doloremque laudantium, totam rem aperiam, eaque ipsa quae ab illo inventore veritatis et quasi architecto beatae vitae dicta.</p></div>
    <div class="dish-photo" role="img" aria-label="Chopping board with herbs and vegetables" style="background:linear-gradient(135deg,#3a2a22,#8a6a4a 50%,#c9b9a6)"></div>
    <div class="dish"><p class="dish-price">$22.50</p><h3 class="dish-name">Kiddy's Special</h3><p class="dish-desc">Sed ut perspiciatis unde omnis iste natus error sit voluptatem accusantium doloremque laudantium, totam rem aperiam, eaque ipsa quae ab illo inventore veritatis et quasi architecto beatae vitae dicta.</p></div>

    <div class="dish-photo" role="img" aria-label="Toasted bread topped with greens" style="background:linear-gradient(135deg,#c9cfc4,#7a9a4a 50%,#b7bcb2)"></div>
    <div class="dish"><h3 class="dish-name gold">ASK YOUR WAITER</h3><p class="dish-desc">Sed ut perspiciatis unde omnis iste natus error sit voluptatem accusantium doloremque laudantium, totam rem aperiam, eaque ipsa quae ab illo inventore veritatis et quasi architecto beatae vitae dicta.</p></div>
    <div class="dish-photo" role="img" aria-label="Halved pomegranate on a dark surface" style="background:linear-gradient(135deg,#141414,#6a1420 50%,#1a1a1a)"></div>
  </div>
</section>

<section class="reviews">
  <span class="menu-link">View Our Full Menu</span>
  <h2 class="reviews-title">What Our Customers Say</h2>
  <div class="review-row">
    <article>
      <svg class="stars" width="140" height="20" viewBox="0 0 140 20"><g fill="#c9a15a"><path id="s" d="M10 1l2.6 6 6.4.5-4.9 4.2 1.5 6.3L10 14.6 4.4 18l1.5-6.3L1 7.5l6.4-.5z"/><use href="#s" x="29"/><use href="#s" x="58"/><use href="#s" x="87"/><use href="#s" x="116"/></g></svg>
      <h3 class="review-title">"A Great Find"</h3>
      <p class="review-text">"Lorem ipsum dolor sit amet, consectetur adipiscing elit. Aliquam eu ante eu lectus ornare porta."</p>
    </article>
    <article>
      <svg class="stars" width="140" height="20" viewBox="0 0 140 20"><g fill="#c9a15a"><use href="#s"/><use href="#s" x="29"/><use href="#s" x="58"/><use href="#s" x="87"/><use href="#s" x="116"/></g></svg>
      <h3 class="review-title">"Fabulous food &amp; flawless service"</h3>
      <p class="review-text">"Lorem ipsum dolor sit amet, consectetur adipiscing elit. Aliquam eu ante eu lectus ornare porta."</p>
    </article>
    <article>
      <svg class="stars" width="140" height="20" viewBox="0 0 140 20"><g fill="#c9a15a"><use href="#s"/><use href="#s" x="29"/><use href="#s" x="58"/><use href="#s" x="87"/><use href="#s" x="116"/></g></svg>
      <h3 class="review-title">"Another successful experience"</h3>
      <p class="review-text">"Lorem ipsum dolor sit amet, consectetur adipiscing elit. Aliquam eu ante eu lectus ornare porta."</p>
    </article>
    <article>
      <svg class="stars" width="140" height="20" viewBox="0 0 140 20"><g fill="#c9a15a"><use href="#s"/><use href="#s" x="29"/><use href="#s" x="58"/><use href="#s" x="87"/><use href="#s" x="116"/></g></svg>
      <h3 class="review-title">"Speechless"</h3>
      <p class="review-text">"Lorem ipsum dolor sit amet, consectetur adipiscing elit. Aliquam eu ante eu lectus ornare porta."</p>
    </article>
  </div>
</section>

<section class="info" role="img" aria-label="Dim photo of guests gathered in the bar">
  <div class="info-shade"></div>
  <div class="info-card hours">
    <h3 class="info-heading">Hours of Operation</h3>
    <p class="info-day">MON – FRI</p>
    <p class="info-line">11:00am – 3:00pm<br>4:00pm – 10:00pm</p>
    <p class="info-day">SAT</p>
    <p class="info-line">3:00pm – 10:00pm</p>
    <p class="info-day">SUN</p>
    <p class="info-line">We are closed</p>
  </div>
  <div class="info-card visit">
    <h3 class="info-heading">Visit Us</h3>
    <p class="info-line">Address</p>
    <p class="info-line">Address</p>
    <p class="info-line">Address</p>
    <h3 class="info-heading" style="margin-top:26px">Call Us</h3>
    <p class="info-line">000.000.0000</p>
  </div>
</section>

<footer class="site-footer">
  <div class="footer-brand">DUNMORE'S</div>
  <div class="footer-col faq">
    <h4>FAQ</h4>
    <p>Q: Lorem ipsum?</p><p>Q: Lorem ipsum?</p><p>Q: Lorem ipsum?</p><p>Q: Lorem ipsum?</p><p>Q: Lorem ipsum?</p><p>Q: Lorem ipsum?</p>
    <p>(Click here to read more FAQs)</p>
  </div>
  <div class="footer-col meal">
    <h4>Meal Of The Week</h4>
    <div class="meal-photo" role="img" aria-label="Plated dish of the week"></div>
    <p class="meal-caption">Homemade flatbread with greens and herbs</p>
  </div>
  <div class="footer-col contact">
    <h4>Contact Us</h4>
    <p>Address</p><p>Address</p><p>Address</p><p>Call: 000-000-0000</p>
    <div class="socials"><span></span><span></span><span></span><span></span><span></span></div>
  </div>
</footer>

<div class="footer-bar">© 2024 Dunmore's. All rights reserved.</div>

</body>
</html>
```